sydney wedding photography business needs a business card design

we need a business card design for a sydney based wedding photography and videography business. our business name is :golden hour photography and video. our target clients are 24-35 yrs female. our style is candid, organic, natural, dynamic. we are a team of young photographers and videographers, and help brides to create memories that they will cherish for the rest of their lives. the logo will be provided. we want an elegant design that reflects our style, and also want to give a great impression to our clients that we are one of the best studios in sydney and our brand means quality and premium service.

Target Market(s)

bride to be, 24-35 years old, living in sydney and surrunding areas

Industry/Entity Type

Wedding Photography

Contact Information for Business Card

address: 57 marrow lane, bexton nsw 2041
mobile: 0431872056
phone: (02) 9361 2748
info@goldenhourstudio.net.au
www.goldenhourstudio.net.au
facebook:goldenhourbridals
instagram:goldenhourbridals

Font styles to use
Serif
Sans Serif

Requirements
Nice to have
• maybe add my slogan"memories beyond eternity" if the layout looks good
Should not have
• no black color, not good idea for wedding biz card

```html
<!DOCTYPE html>
<html lang="en">
<head>
<meta charset="utf-8">
<title>Golden Hour Photography and Video – Business Card</title>
<link rel="stylesheet" href="https://fonts.googleapis.com/css2?family=Jost:wght@400;500&display=swap">
<style>
  :root {
    --backdrop: #e9e5dd;
    --ink: #2e2a24;
    --header-deep: #3a2812;
    --header-soft: #5e4322;
    --gold: #c8961c;
    --gold-light: #e2b640;
    --gold-deep: #9c7112;
    --paper: #ffffff;
    --motif: #efece6;
  }
  * { margin: 0; padding: 0; box-sizing: border-box; }
  html, body { width: 1200px; height: 950px; overflow: hidden; }
  body {
    background: var(--backdrop);
    font-family: "Jost", "Helvetica Neue", Arial, sans-serif;
    position: relative;
  }
  .card {
    position: absolute;
    left: 250px;
    width: 700px;
    height: 400px;
    border-radius: 4px;
    overflow: hidden;
    box-shadow: 0 10px 30px rgba(0,0,0,.18);
  }
  .card--front { top: 55px; background: var(--paper); }
  .card--back {
    top: 495px;
    background: linear-gradient(135deg, var(--gold-deep) 0%, var(--gold) 45%, var(--gold-light) 100%);
  }
  .card__shapes { position: absolute; inset: 0; width: 100%; height: 100%; }
  .brand-name {
    position: absolute;
    top: 62px;
    left: 0;
    width: 100%;
    text-align: center;
    padding-left: 110px;
    white-space: nowrap;
    font-size: 21px;
    font-weight: 500;
    letter-spacing: 2px;
    text-transform: uppercase;
    color: var(--gold-light);
  }
  .contact {
    position: absolute;
    left: 34px;
    top: 172px;
    color: var(--ink);
  }
  .contact__name {
    font-size: 24px;
    font-weight: 400;
    letter-spacing: 1px;
    color: var(--gold);
    text-transform: uppercase;
    line-height: 1.05;
  }
  .contact__role {
    font-size: 15px;
    letter-spacing: 1px;
    text-transform: uppercase;
    line-height: 1.2;
    margin-bottom: 7px;
  }
  .contact__address { font-size: 13.5px; line-height: 1.3; margin-bottom: 7px; }
  .contact__list { list-style: none; font-size: 13.5px; line-height: 1.38; }
  .contact__list li { display: flex; align-items: center; gap: 8px; }
  .contact__icon { width: 12px; height: 12px; flex: none; }
</style>
</head>
<body>

<section class="card card--front" aria-label="Business card front">
  <svg class="card__shapes" viewBox="0 0 700 400" preserveAspectRatio="none">
    <defs>
      <linearGradient id="headerFill" x1="0" y1="0" x2="1" y2="1">
        <stop offset="0" stop-color="var(--header-soft)"/>
        <stop offset="0.6" stop-color="var(--header-deep)"/>
      </linearGradient>
      <linearGradient id="swooshFill" x1="0" y1="0" x2="1" y2="0">
        <stop offset="0" stop-color="var(--gold-deep)"/>
        <stop offset="0.5" stop-color="var(--gold)"/>
        <stop offset="1" stop-color="var(--gold-light)"/>
      </linearGradient>
      <radialGradient id="motifFill">
        <stop offset="0" stop-color="var(--motif)"/>
        <stop offset="1" stop-color="var(--paper)"/>
      </radialGradient>
    </defs>
    <ellipse cx="330" cy="300" rx="120" ry="95" fill="url(#motifFill)" role="img" aria-label="Faint decorative brand motif"/>
    <path class="card__swoosh" d="M0,122 C250,115 520,142 700,205 L700,218 C520,160 250,142 0,150 Z" fill="url(#swooshFill)"/>
    <path class="card__rule" d="M0,150 C250,142 520,160 700,218" fill="none" stroke="var(--header-deep)" stroke-width="1.5"/>
    <path class="card__header" d="M0,0 H700 V205 C520,142 250,115 0,122 Z" fill="url(#headerFill)"/>
  </svg>

  <p class="brand-name">Golden Hour Photography and Video</p>

  <div class="contact">
    <h1 class="contact__name">Amelia Hart</h1>
    <p class="contact__role">Photographer</p>
    <p class="contact__address">57 marrow lane<br>bexton nsw 2041</p>
    <ul class="contact__list">
      <li>
        <svg class="contact__icon" viewBox="0 0 12 12" aria-hidden="true"><path d="M2.5 1 L4.5 3.2 L3.4 4.4 C4.2 6 5.9 7.7 7.6 8.6 L8.8 7.5 L11 9.5 L9.6 11 C5.5 10.5 1.5 6.5 1 2.4 Z" fill="var(--gold)"/></svg>
        (02) 9361 2748
      </li>
      <li>
        <svg class="contact__icon" viewBox="0 0 12 12" aria-hidden="true"><rect x="3" y="0.5" width="6" height="11" rx="1" fill="none" stroke="var(--gold)" stroke-width="1.3"/><rect x="5" y="9" width="2" height="1" fill="var(--gold)"/></svg>
        (04) 3187 2056
      </li>
      <li>
        <svg class="contact__icon" viewBox="0 0 12 12" aria-hidden="true"><rect width="12" height="12" rx="1.5" fill="var(--gold)"/><path d="M2.5 4 L6 6.8 L9.5 4" fill="none" stroke="var(--paper)" stroke-width="1.1"/></svg>
        info@goldenhourstudio.net.au
      </li>
      <li>
        <svg class="contact__icon" viewBox="0 0 12 12" aria-hidden="true"><rect width="12" height="12" rx="1.5" fill="var(--gold)"/><circle cx="6" cy="6" r="3.3" fill="none" stroke="var(--paper)" stroke-width="1"/></svg>
        goldenhourstudio.net.au
      </li>
      <li>
        <svg class="contact__icon" viewBox="0 0 12 12" aria-hidden="true"><rect width="12" height="12" rx="1.5" fill="var(--gold)"/></svg>
        goldenhourbridals
      </li>
      <li>
        <svg class="contact__icon" viewBox="0 0 12 12" aria-hidden="true"><rect width="12" height="12" rx="1.5" fill="var(--gold)"/></svg>
        goldenhourbridals
      </li>
    </ul>
  </div>
</section>

<section class="card card--back" aria-label="Business card back"></section>

</body>
</html>
```